Web page for organic mosquito control company in Texas

Looking for a webpage that communicates the three main objectives of the company: Guaranteed effective, Affordable Rates, Organic Solution.
The company specializes in safe organic mosquito control. Service is conducted monthly during the mosquito season. What makes Quillmoor unique is the fact that it does not employ heavy pesticides, expensive equipment purchases and no nozzles misting installed throughout the property. I have some videos that I want to integrate. Please specify what format and codec do want the multi media file in?
Target Market(s)
Mothers 30-55 years of age
Industry/Entity Type
It Company
Number of Pages Required
5+ page
Requirements
Must have
- Predominant space for video on the home page
Nice to have
- Environmental theme without overdoing it.

```html
<!DOCTYPE html>
<html lang="en">
<head>
<meta charset="utf-8">
<title>Quillmoor Mosquito Control</title>
<link href="https://fonts.googleapis.com/css2?family=Open+Sans:wght@400;600;700&family=Arimo:wght@400;700&display=swap" rel="stylesheet">
<style>
:root{
  --green:#9ccb3b;
  --green-light:#c8e08a;
  --green-dark:#4e8a1e;
  --orange:#e08a0e;
  --dark:#2e2e2e;
  --footer:#393939;
  --text:#333;
  --muted:#666;
  --white:#fff;
  --cream:#ffe9b8;
}
*{margin:0;padding:0;box-sizing:border-box}
html,body{width:1200px;height:2445px;overflow:hidden;background:#fff}
body{position:relative;font-family:Arimo,Arial,sans-serif;color:var(--text);font-size:12px}
.abs{position:absolute}
.heading{font-family:"Open Sans",Arial,sans-serif;font-weight:400}

/* header */
.site-header{position:absolute;left:0;top:0;width:1200px;height:100px;background:linear-gradient(#fff 0%,rgba(255,255,255,.85) 70%,rgba(255,255,255,0));z-index:2}
.brand{position:absolute;left:72px;top:16px;display:flex;align-items:center;gap:8px}
.brand-mark{width:14px;height:14px;background:var(--green-dark)}
.brand-name{font-family:"Open Sans",sans-serif;font-weight:700;font-size:24px;line-height:26px;color:var(--green-dark);width:130px}
.main-nav{position:absolute;right:78px;top:38px;display:flex;gap:30px;font-family:"Open Sans",sans-serif;font-size:14px;color:#444}
.main-nav .drop:after{content:"";display:inline-block;width:4px;height:4px;border-right:1.5px solid #444;border-bottom:1.5px solid #444;transform:rotate(45deg);margin:0 0 3px 4px}

/* hero */
.hero{position:absolute;left:0;top:0;width:1200px;height:450px;background:linear-gradient(100deg,#8fae5a 0%,#c9d9a8 22%,#e9d2b6 40%,#d9b592 52%,#6f9a4a 68%,#b7cfa0 82%,#e6e6e6 100%)}
.hero-fade{position:absolute;left:0;bottom:0;width:100%;height:30px;background:linear-gradient(rgba(255,255,255,0),rgba(255,255,255,.7))}
.hero-tag{position:absolute;left:31px;top:312px;width:452px;height:62px;background:rgba(86,170,84,.9);color:#fff;font-family:"Open Sans",sans-serif;font-size:44px;line-height:62px;padding-left:18px}

/* intro */
.intro{position:absolute;left:0;top:450px;width:1200px;height:410px;background:var(--green-light)}
.intro-title{left:67px;width:518px;top:36px;text-align:center;font-size:31px;color:#fff}
.intro-text{left:67px;width:518px;top:84px;font-size:12px;line-height:16px;text-align:justify;color:#333}
.intro-text p{margin-bottom:14px}
.btn-orange{display:inline-block;background:var(--orange);color:#fff;border-radius:3px;font-size:11px;font-weight:700;text-align:center}
.intro-more{left:282px;top:318px;width:76px;height:30px;line-height:30px}
.video-title{left:619px;width:514px;top:36px;font-size:31px;color:#eef5dc}
.video{left:619px;top:83px;width:514px;height:291px;background:radial-gradient(circle at 50% 55%,#a06a3a 0%,#5a3b28 25%,#2a2f35 55%,#15171a 100%)}
.video-label{left:12px;top:8px;color:#fff;font-size:12px}
.video-share{right:10px;top:6px}

/* how it works */
.how{position:absolute;left:0;top:860px;width:1200px;height:400px;background:var(--dark);color:#fff}
.how-title{left:0;width:1200px;top:8px;text-align:center;font-size:32px}
.how-lead{left:67px;width:1066px;top:56px;font-size:12px;line-height:17px;color:var(--cream)}
.features{left:51px;top:125px;width:1098px;height:240px;display:flex}
.feature{flex:1;text-align:center;padding:0 22px;border-left:1px solid #555}
.feature:first-child{border-left:none}
.feature-icon{width:52px;height:52px;background:var(--orange);border-radius:3px;margin:0 auto;display:flex;align-items:center;justify-content:center}
.feature-title{font-family:"Open Sans",sans-serif;font-size:20px;line-height:23px;margin-top:20px}
.feature-text{font-size:12px;line-height:19px;margin-top:10px;height:84px}
.feature-text.italic{font-style:italic}
.feature-more{color:var(--orange);font-size:11px;margin-top:6px}

/* birth + contact */
.story{position:absolute;left:0;top:1277px;width:1200px;height:443px;background:var(--green);color:#222}
.to-top{width:28px;height:28px;border-radius:50%;background:#d9b36a;display:flex;align-items:center;justify-content:center}
.story-title{left:67px;width:568px;top:40px;text-align:center;font-size:21px;color:#fff}
.story-text{left:67px;width:699px;top:84px;font-size:12px;line-height:18px}
.story-text p{margin-bottom:10px}
.story-more{padding:0 10px;height:26px;line-height:26px;margin-left:4px}
.faq-btn{top:295px;height:41px;border:2px solid #fff;border-radius:3px;color:#fff;font-weight:700;font-size:16px;line-height:37px;text-align:center}
.reach-title{left:800px;width:333px;top:38px;text-align:center;font-size:34px;color:#fff}
.form-group{left:800px;top:91px;width:333px;background:#fff;border-radius:3px}
.field{height:36px;border-bottom:1px solid #ddd;padding-left:10px;line-height:36px;color:#777;font-size:13px;position:relative}
.field:last-child{border-bottom:none}
.field i{position:absolute;right:12px;top:15px;width:7px;height:7px;border:1px solid #bbb;border-radius:2px}
.message{left:800px;top:216px;width:333px;height:134px;background:#fff;border-radius:3px;padding:10px;color:#777;font-size:13px}
.send{left:800px;top:369px;width:96px;height:25px;line-height:25px;border-radius:2px;font-weight:400}
.clear{left:1090px;top:372px;color:#d0a04a;font-size:11px}

/* content row */
.rule{position:absolute;left:0;width:1200px;height:1px;background:#ccc}
.col-title{font-family:"Open Sans",sans-serif;font-size:16px;color:#333;text-transform:uppercase}
.testimonial{left:67px;top:1800px;width:332px;height:226px;border:1px solid #bbb;border-radius:4px;padding:22px 18px;font-size:12px;line-height:20px;color:#333}
.avatar{width:42px;height:42px;border-radius:50%;background:linear-gradient(#3a3a3a,#c98a5e)}
.dots{left:220px;top:2036px;font-size:10px;color:#999;letter-spacing:2px}
.post{left:434px;width:332px;display:flex;gap:18px;align-items:flex-start}
.post-thumb{width:52px;height:52px;border-radius:50%;flex:none}
.post-title{font-size:13px;line-height:20px;color:#333}
.post-date{font-size:10px;color:#555;margin-top:6px}
.gallery-main{left:800px;top:1800px;width:248px;height:188px;background:linear-gradient(#d7dde6 0%,#c2cad6 45%,#eef1f5 100%)}
.gallery-next{left:1068px;top:1800px;width:65px;height:188px;background:linear-gradient(#e4e6e8,#b6a18a)}
.gallery-arrow{left:1100px;top:1873px;width:24px;height:40px;background:var(--orange);border-radius:3px;display:flex;align-items:center;justify-content:center}

/* footer */
.footer{position:absolute;left:0;top:2098px;width:1200px;height:254px;background:var(--footer);color:#ddd}
.foot-col{top:43px;width:250px}
.foot-col h3{font-family:"Open Sans",sans-serif;font-weight:400;font-size:16px;color:#ddd;margin-bottom:17px}
.foot-col li{list-style:none;font-size:12px;line-height:19.5px;color:#e6e6e6}
.bottom{position:absolute;left:0;top:2352px;width:1200px;height:93px;background:#f2f2f2}
.bottom .brand{top:22px}
.powered{left:223px;top:43px;font-size:10px;color:#777}
</style>
</head>
<body>

<section class="hero" role="img" aria-label="Photo of a smiling family with two children relaxing outdoors among green garden plants">
  <div class="hero-fade"></div>
  <div class="hero-tag">Guaranteed effective</div>
</section>

<header class="site-header">
  <div class="brand"><span class="brand-mark"></span><span class="brand-name">Quillmoor Mosquito</span></div>
  <nav class="main-nav">
    <span>HOME</span><span class="drop">ABOUT US</span><span class="drop">QUILLMOOR SOLUTION</span><span class="drop">PRICE</span><span class="drop">HOW IT WORKS ?</span><span class="drop">F A Q</span><span>CONTACT</span>
  </nav>
</header>

<section class="intro">
  <h2 class="abs heading intro-title">Mosquito Freedom!</h2>
  <div class="abs intro-text">
    <p>Designed in Texas by Texans, specifically for Texas Mosquitoes, the Quillmoor Mosquito Control System is the first organically-based mosquito control system that eliminates both mosquitoes and the need for automatic mosquito misting systems.Our 99.5% organic solution not only minimizes your family's risk to harmful pathogens such as West Nile Virus, Chikungunya, and Eastern Equine Encephalitis, but it also reduces pesticide exposure by 95% compared to nozzle misting systems. Better yet, our customer's report the Quillmoor system is nearly twice as effective as expensive nozzle systems.Throw away the sprays, magnets, fans, and other gimmicks that offer little in effectiveness.</p>
    <p>The Quillmoor Mosquito Control System is the only effective and guaranteed method of ridding those annoying mosquitoes, protecting your health, and enjoying your outdoor living environment to the fullest.</p>
  </div>
  <span class="abs btn-orange intro-more">read more</span>
  <h2 class="abs heading video-title">Watch the video</h2>
  <div class="abs video" role="img" aria-label="Video player showing a magnified close-up of a mosquito">
    <span class="abs video-label">Mosquito Week</span>
    <svg class="abs video-share" width="14" height="14" viewBox="0 0 14 14"><circle cx="10" cy="3" r="2" fill="#fff"/><circle cx="3" cy="7" r="2" fill="#fff"/><circle cx="10" cy="11" r="2" fill="#fff"/><path d="M10 3 3 7 10 11" stroke="#fff" fill="none" stroke-width="1.2"/></svg>
  </div>
</section>

<section class="how">
  <h2 class="abs heading how-title">How the Quillmoor Mosquito Control System works</h2>
  <p class="abs how-lead">Mosquitoes have four distinct life stages (egg, larvae, pupae, adult). Most mosquito control methods fail to control mosquito populations by focusing inadequately ononlyone of these life stages. The Quillmoor Mosquito Control System focuseson the eradication of allfourlife stages to achieve 90%+ eradication of the mosquito population on a property</p>
  <div class="abs features">
    <div class="feature">
      <div class="feature-icon"><svg width="26" height="26" viewBox="0 0 26 26"><circle cx="11" cy="11" r="7" stroke="#fff" stroke-width="3" fill="none"/><path d="M16 16l7 7" stroke="#fff" stroke-width="3.5" stroke-linecap="round"/></svg></div>
      <h3 class="feature-title">Remedying Conducive Conditions</h3>
      <p class="feature-text">Before a service can commence, a licensed technician will inspect and identify areas to be addressed that are contributing to mosquito harborages..</p>
      <p class="feature-more">read more &rsaquo;</p>
    </div>
    <div class="feature">
      <div class="feature-icon"><svg width="26" height="26" viewBox="0 0 26 26"><circle cx="13" cy="13" r="9" stroke="#fff" stroke-width="3" fill="none"/><path d="M7 7l12 12" stroke="#fff" stroke-width="3"/></svg></div>
      <h3 class="feature-title">Eradication of adult mosquitoes</h3>
      <p class="feature-text italic">Utilizing the most powerful equipment available, technicians direct a pyrethrum-based adulticide deep into mosquito harborages at a velocity of 140 mph</p>
      <p class="feature-more">read more &rsaquo;</p>
    </div>
    <div class="feature">
      <div class="feature-icon"><svg width="26" height="26" viewBox="0 0 26 26"><path d="M9 3h8M11 3v7l-6 11a2 2 0 0 0 2 3h12a2 2 0 0 0 2-3l-6-11V3" stroke="#fff" stroke-width="2.5" fill="none" stroke-linejoin="round"/><path d="M8 17h10l2 5H6z" fill="#fff"/></svg></div>
      <h3 class="feature-title">Repelling adult mosquitoes</h3>
      <p class="feature-text">A mixture of unique essential oils in the Quillmoor solution serve as a strong repellant, preventing mosquitoes from nesting on the property.</p>
      <p class="feature-more">read more &rsaquo;</p>
    </div>
    <div class="feature">
      <div class="feature-icon"><svg width="26" height="26" viewBox="0 0 26 26"><path d="M5 13l6 6L22 7" stroke="#fff" stroke-width="4" fill="none" stroke-linecap="round" stroke-linejoin="round"/></svg></div>
      <h3 class="feature-title">Sterilizing mosquito larvae</h3>
      <p class="feature-text">When standing water cannot be remedied, the Quillmoor Mosquito Control System utilizes insect-growth-regulators, to treat water receptacles</p>
      <p class="feature-more">read more &rsaquo;</p>
    </div>
  </div>
</section>

<section class="story">
  <div class="abs to-top" style="left:1157px;top:-7px"><svg width="10" height="8" viewBox="0 0 10 8"><path d="M1 6l4-4 4 4" stroke="#fff" stroke-width="1.6" fill="none"/></svg></div>
  <h2 class="abs heading story-title">The Birth of the Quillmoor Mosquito Control System</h2>
  <div class="abs story-text">
    <p>The company's founders, Dale Orwin and Martin Heale have been in the pest control business since 1996. Understanding the life cycles, environments, and habits of all household pests have resulted in effective treatments designed to eliminate pests while minimizing pesticide exposure to their customers. Continually seeking for ways to improve their service led them to their discovery of the Quillmoor Mosquito Control System.</p>
    <p>What initially motivated the founders is that they are parents of small children and found themselves frustrated with the hazards and annoyance of mosquitoes at their own homes, and the inadequate solutions available to the public.</p>
    <p>This propelled the founders into a quest to find a productto tackle the problem of mosquitoes that was</p>
    <p>1) Effective 2) Affordable 3) Natural and 4) Safe<span class="btn-orange story-more">read more ..</span></p>
  </div>
  <div class="abs faq-btn" style="left:67px;width:147px">SERVICE F A Q</div>
  <div class="abs faq-btn" style="left:312px;width:163px">MOSQUITO F A Q</div>
  <div class="abs faq-btn" style="left:557px;width:146px">DISEASE F A Q</div>

  <h2 class="abs heading reach-title">Reach to us</h2>
  <div class="abs form-group">
    <div class="field">Name *<i></i></div>
    <div class="field">E-mail *<i></i></div>
    <div class="field">Telephone<i></i></div>
  </div>
  <div class="abs message">Message *</div>
  <span class="abs btn-orange send">Send message</span>
  <span class="abs clear">clear &#8855;</span>
</section>

<div class="rule" style="top:1731px"></div>

<h3 class="abs col-title" style="left:67px;top:1771px">Client Testimonial</h3>
<div class="abs testimonial">
  <p>Lorem Ipsum is simply dummy text of the printing and typesetting industry. Lorem Ipsum has been the industry's standard dummy text ever since the 1500s, when an unknown printer took a galley of type and scrambled it to make a type specimen book. It has survived not only five centuries,</p>
  <div style="display:flex;align-items:center;gap:16px;margin-top:20px">
    <div class="avatar" role="img" aria-label="Client portrait"></div><span>Anika &ndash; UAE</span>
  </div>
</div>
<div class="abs dots">&bull;&bull;&bull;</div>

<h3 class="abs col-title" style="left:434px;top:1771px">Blogs &amp; News</h3>
<div class="abs post" style="top:1806px">
  <div class="post-thumb" role="img" aria-label="Illustration of mosquito-borne disease" style="background:linear-gradient(#f3f3f3,#d8c8b8)"></div>
  <div><p class="post-title">Learn More About Mosquito-Borne Diseases</p><p class="post-date">February 16, 2015</p></div>
</div>
<div class="abs" style="left:434px;top:1874px;width:332px;height:1px;background:#bbb"></div>
<div class="abs post" style="top:1890px">
  <div class="post-thumb" role="img" aria-label="Photo of a garden around a home" style="background:linear-gradient(#7a9a5a,#3f5a2f)"></div>
  <div><p class="post-title">Learn How To Control Mosquitoes Around Your Home</p><p class="post-date">February 16, 2015</p></div>
</div>

<h3 class="abs col-title" style="left:800px;top:1771px">Photo Gallery</h3>
<div class="abs gallery-main" role="img" aria-label="Gallery photo of people ice skating outdoors"></div>
<div class="abs gallery-next" role="img" aria-label="Gallery photo of a bottle on a table"></div>
<div class="abs gallery-arrow"><svg width="8" height="12" viewBox="0 0 8 12"><path d="M2 1l5 5-5 5" stroke="#fff" stroke-width="2" fill="none"/></svg></div>

<div class="rule" style="top:2057px"></div>

<footer class="footer">
  <div class="abs foot-col" style="left:67px">
    <h3>CONTACT ADDRESS</h3>
    <ul><li>Quillmoor Mosquitos</li><li>Linden Road, 8th street</li><li>Canada, abc /1234</li><li>Phone : 555 010 2040</li><li>email - info@quillmoor.com</li><li>Web - www.quillmoor.com</li></ul>
  </div>
  <div class="abs foot-col" style="left:343px">
    <h3>HELP DESK &amp; SUPPORT</h3>
    <ul><li>Sales Enquiry</li><li>Customer Support</li><li>Get Free quote</li><li>Talk to Sales Expert</li><li>Order Online</li><li>Get Free quote</li></ul>
  </div>
  <div class="abs foot-col" style="left:619px">
    <h3>DOWNLOADS</h3>
    <ul><li>Broucher Downloads</li><li>Broucher Downloads</li><li>Broucher Downloads</li><li>Broucher Downloads</li><li>Broucher Downloads</li></ul>
  </div>
  <div class="abs foot-col" style="left:893px">
    <h3>QUICK LINK</h3>
    <ul><li>Sales Enquiry</li><li>Customer Support</li><li>Get Free quote</li><li>Talk to Sales Expert</li><li>Order Online</li><li>Get Free quote</li></ul>
  </div>
</footer>

<div class="bottom">
  <div class="brand"><span class="brand-mark"></span><span class="brand-name">Quillmoor Mosquito</span></div>
  <span class="abs powered">Powered By : webnorth</span>
  <div class="abs to-top" style="left:1157px;top:44px"><svg width="10" height="8" viewBox="0 0 10 8"><path d="M1 6l4-4 4 4" stroke="#fff" stroke-width="1.6" fill="none"/></svg></div>
</div>

</body>
</html>
```